Electrical needs letterhead design

Need a letterhead design for an electrical company. Using the same colours as to what are used in the logo.
After a modern design.

Want the logo in top right or top left.

Must include...

ABN 71 804 239 356
PHONE 0458203917
www.kelmaroo.com.au
jed@kelmaroo.com.au

'ABN' and 'PHONE' in bold.

Keep it basic. Logo top left, details either next to it or far right corner. Dont want any other objects included.

Electrical

```html
<!DOCTYPE html>
<html lang="en">
<head>
<meta charset="utf-8">
<title>Kelmaroo Letterhead</title>
<link rel="stylesheet" href="https://fonts.googleapis.com/css2?family=Source+Sans+3:wght@400;700&family=Oswald:wght@400;600&family=Pinyon+Script&display=swap">
<style>
  :root {
    --brand-red: #a3281f;
    --band-dark: #7a1913;
    --band-bright: #d8412e;
    --ink: #111111;
    --paper: #ffffff;
    --label: #000000;
  }
  * { margin: 0; padding: 0; box-sizing: border-box; }
  html, body { width: 848px; height: 1200px; overflow: hidden; background: var(--paper); }
  .letterhead {
    position: relative;
    width: 848px;
    height: 1200px;
    background: var(--paper);
    font-family: "Source Sans 3", "Helvetica Neue", Arial, sans-serif;
    color: var(--ink);
  }
  .brand {
    position: absolute;
    top: 48px;
    right: 22px;
    display: flex;
    align-items: center;
    gap: 12px;
  }
  .brand-dot {
    width: 28px; height: 28px;
    border-radius: 50%;
    background: var(--brand-red);
  }
  .brand-name {
    font-family: "Source Sans 3", "Helvetica Neue", Arial, sans-serif;
    font-weight: 400;
    font-size: 60px;
    line-height: 1;
    color: var(--brand-red);
  }
  .salutation {
    position: absolute;
    left: 50px;
    top: 244px;
    font-size: 18.5px;
    font-weight: 700;
  }
  .body-text p {
    position: absolute;
    left: 50px;
    width: 790px;
    font-size: 16px;
    line-height: 23.5px;
    letter-spacing: -0.1px;
  }
  .p1 { top: 286px; }
  .p2 { top: 392px; }
  .p3 { top: 485px; }
  .p4 { top: 619px; }
  .p5 { top: 670px; }
  .signature {
    position: absolute;
    left: 476px;
    top: 862px;
    font-family: "Pinyon Script", cursive;
    font-size: 60px;
    line-height: 1;
  }
  .sign-role {
    position: absolute;
    left: 624px;
    top: 934px;
    font-size: 22px;
  }
  .contact-band {
    position: absolute;
    left: 0; bottom: 0;
    width: 848px;
    height: 46px;
    background: linear-gradient(90deg, #ffffff 0px, var(--band-dark) 70px, var(--band-bright) 210px, var(--band-bright) 100%);
    font-family: "Oswald", "Arial Narrow", sans-serif;
    font-size: 14.5px;
    color: var(--paper);
  }
  .band-dot {
    position: absolute;
    left: 4px; top: 8px;
    width: 46px; height: 46px;
    border-radius: 50%;
    background: var(--brand-red);
  }
  .contact-item {
    position: absolute;
    top: 12px;
    white-space: nowrap;
  }
  .contact-item b { color: var(--label); font-weight: 600; }
  .item-abn { left: 93px; }
  .item-phone { left: 249px; }
  .item-email { left: 408px; }
  .item-web { right: 20px; }
</style>
</head>
<body>
<div class="letterhead">
  <header class="brand">
    <span class="brand-dot"></span>
    <span class="brand-name">Kelmaroo</span>
  </header>

  <h1 class="salutation">Lorem ipsum dolor,</h1>

  <section class="body-text">
    <p class="p1">Lorem ipsum dolor sit amet, consectetur adipisicing elit, sed do eiusmod tempor incididunt ut<br>magna aliqua. Ut enim ad minim veniam, quis nostrud exercitation ullamco laboris nisi ut aliqu.</p>
    <p class="p2">Lorem ipsum dolor sit amet, consectetur adipisicing elit, sed do eiusmod tempor incididunt<br>magna aliqua. Ut enim ad minim veniam, quis nostrud exercitation.</p>
    <p class="p3">Lorem ipsum dolor sit amet, consectetur adipisicing elit, sed do eiusmod tempor incididunt<br>magna aliqua. Ut enim ad minim veniam, quis nostrud exercitation ullamco laboris nisi ut al<br>do consequa.Lorem ipsum dolor sit amet, consectetur adipisicing elit, sed do eiusmod temp<br>bore et dolore magna aliqua. Ut enim ad minim veniam, quis.</p>
    <p class="p4">Lorem ipsum dolor sit amet, consectetur adipisicing elit, sed do eiusmod tempor incididunt.</p>
    <p class="p5">Lorem ipsum dolor sit amet, consectetur adipisicing elit, sed do eiusmod tempor incididunt<br>magna aliqua. Ut enim ad minim veniam, quis nostrud exercitation ullamco laboris nisi ut al<br>do consequa.Lorem ipsum dolor sit amet, consectetur adipisicing elit, sed do eiusmod temp<br>bore et dolore magna aliqua. Ut enim ad minim veniam, quis.</p>
  </section>

  <div class="signature">Your Name</div>
  <div class="sign-role">Director</div>

  <footer class="contact-band">
    <span class="band-dot"></span>
    <span class="contact-item item-abn"><b>ABN:</b> 71 804 239 356</span>
    <span class="contact-item item-phone"><b>PHONE:</b> 0458203917</span>
    <span class="contact-item item-email"><b>Email:</b> jed@kelmaroo.com.au</span>
    <span class="contact-item item-web"><b>Web:</b> www.kelmaroo.com.au</span>
  </footer>
</div>
</body>
</html>
```